Proposal Poster, posters for kids to hold

I am proposing to my girlfriend soon, I need two posters made for my kids to hold one I want to say “be my mommy”
And the other “will you marry my daddy”
Both in horizontal format. I plan on sending the files to a print shop to get them printed on a large poster. Simple is fine with maybe a few graphics. Open to anything. Kids will be holding it from the beach as we are on a jet ski close to shore. Must be readable font from a short distance

• Cute but readable font from a distance

```html
<!DOCTYPE html>
<html lang="en">
<head>
<meta charset="utf-8">
<title>Proposal Posters</title>
<link href="https://fonts.googleapis.com/css2?family=Sniglet:wght@400&display=swap" rel="stylesheet">
<style>
  :root {
    --page: #ffffff;
    --text: #ffffff;
    --yellow: #f9ea98;
    --aqua: #7fdde3;
    --lilac: #e3bde0;
    --pink: #f6b1d5;
    --rose: #f38cba;
    --hot-pink: #f590b8;
    --violet: #d9a6e4;
  }
  html, body {
    margin: 0;
    padding: 0;
    width: 1200px;
    height: 517px;
    overflow: hidden;
    background: var(--page);
  }
  .canvas {
    position: relative;
    width: 1200px;
    height: 517px;
  }
  .poster {
    position: absolute;
    left: 47px;
    height: 206px;
    display: flex;
    align-items: center;
    overflow: hidden;
  }
  .poster__art {
    position: absolute;
    inset: 0;
  }
  .poster--mommy {
    top: 45px;
    width: 763px;
  }
  .poster--mommy .poster__art {
    background:
      radial-gradient(ellipse 68% 120% at 62% 50%, var(--pink) 0%, var(--lilac) 62%, transparent 64%),
      linear-gradient(90deg, var(--yellow) 0%, var(--yellow) 8%, #bfe3c6 13%, var(--aqua) 22%, var(--aqua) 30%, var(--lilac) 40%, var(--pink) 100%);
  }
  .poster--daddy {
    top: 267px;
    width: 1093px;
  }
  .poster--daddy .poster__art {
    background:
      radial-gradient(ellipse 60% 150% at 48% 20%, var(--rose) 0%, var(--hot-pink) 60%, transparent 62%),
      linear-gradient(90deg, var(--yellow) 0%, var(--yellow) 8%, #f7b8b8 14%, var(--pink) 30%, var(--rose) 60%, var(--hot-pink) 86%, var(--violet) 90%, var(--violet) 100%);
  }
  .poster__text {
    position: relative;
    margin: 0;
    color: var(--text);
    font-family: "Sniglet", sans-serif;
    font-weight: 400;
    font-size: 68px;
    letter-spacing: 1px;
    line-height: 1;
    white-space: nowrap;
  }
  .poster--mommy .poster__text {
    padding-left: 110px;
    margin-top: -24px;
  }
  .poster--daddy .poster__text {
    padding-left: 86px;
    margin-top: -40px;
  }
</style>
</head>
<body>
  <main class="canvas">
    <section class="poster poster--mommy">
      <div class="poster__art" role="img" aria-label="Soft pastel watercolour wash in yellow, aqua, lilac and pink"></div>
      <h1 class="poster__text">Be my mommy</h1>
    </section>
    <section class="poster poster--daddy">
      <div class="poster__art" role="img" aria-label="Soft pastel watercolour wash in yellow, pink and violet"></div>
      <h2 class="poster__text">Will you marry my daddy?</h2>
    </section>
  </main>
</body>
</html>
```